Travelogue book cover

The book is a collection of stories from my travels around the world. These stories run a full range of emotions from unbridled joy, to things that are much funnier today than they were at the time, to moments of sadness while reflecting on places that have been irrevocably changed. This world is an amazing and powerful place, and my stories tell its tale. The overall vibe is to love exploring the world, the thrill of discovery, the comedy of getting outside of your comfort zone, and just generally wanting to convey a sense of wonder and make people feel like they want to get out and explore for themselves.

The audience is in the 30-50 age target, educated, all genders, and either an experienced traveller or wishes they were.

On the style, I am looking for something that stands out when a reader is browsing Pellaro. Since most book covers are bright, full bleed and busy, I would prefer something that emphasizes white space and simplicity.

```html
<!DOCTYPE html>
<html lang="en">
<head>
<meta charset="utf-8">
<title>Stories From My Travels – Book Cover</title>
<link rel="stylesheet" href="https://fonts.googleapis.com/css2?family=Poppins:wght@400;500&display=swap">
<style>
  :root {
    --backdrop: #e6e6e6;
    --paper: #f1f1f1;
    --ink: #2b2b2b;
    --ink-light: #ffffff;
    --meadow: #5a8a44;
    --glacier: #9aa2aa;
    --canyon: #9c5d3a;
    --dune: #c98d5c;
    --dune-light: #d8a77c;
  }
  html, body {
    margin: 0;
    width: 1200px;
    height: 800px;
    overflow: hidden;
    background: var(--backdrop);
    font-family: "Poppins", sans-serif;
  }
  .cover {
    position: absolute;
    left: 360px;
    top: 40px;
    width: 480px;
    height: 720px;
    background: var(--paper);
    overflow: hidden;
  }
  .title { margin: 0; font-weight: 400; }
  .title-line {
    position: absolute;
    left: 72px;
    font-size: 30px;
    font-weight: 400;
    line-height: 1;
    letter-spacing: 0.48em;
    color: var(--ink);
    white-space: nowrap;
    z-index: 2;
  }
  .title-line--stories { top: 220px; }
  .title-line--from { top: 262px; }
  .title-line--my { top: 392px; color: var(--ink-light); }
  .title-line--travels { top: 436px; }
  .landscape-photo {
    position: absolute;
    left: 0;
    top: 290px;
    width: 460px;
    height: 137px;
    z-index: 1;
    background: linear-gradient(90deg,
      var(--meadow) 0%, var(--meadow) 16%,
      var(--glacier) 22%, var(--glacier) 34%,
      var(--canyon) 40%, var(--canyon) 53%,
      var(--dune) 60%, var(--dune-light) 100%);
  }
  .divider {
    position: absolute;
    left: 73px;
    top: 498px;
    width: 37px;
    height: 1px;
    background: var(--ink);
  }
  .author {
    position: absolute;
    left: 73px;
    top: 539px;
    margin: 0;
    font-size: 11.5px;
    font-weight: 500;
    letter-spacing: 0.32em;
    color: var(--ink);
    white-space: nowrap;
  }
</style>
</head>
<body>
  <main class="cover">
    <h1 class="title">
      <span class="title-line title-line--stories">STORIES</span>
      <span class="title-line title-line--from">FROM</span>
      <span class="title-line title-line--my">MY</span>
      <span class="title-line title-line--travels">TRAVELS</span>
    </h1>
    <div class="landscape-photo" role="img" aria-label="Photo collage of landscapes forming one skyline: a green alpine slope, a snowy rock peak, a red sandstone butte and desert dunes with a lone traveller standing on the sand"></div>
    <div class="divider"></div>
    <p class="author">AUTHOR’S NAME</p>
  </main>
</body>
</html>
```